Korimet Business Cards

Korimet is a software startup and we are looking for business cards that help convey our employee personalities, as well as the professionalism of the company.
Our company font is Comfortaa - and the company logo is attached (we are okay having the text beside the logo if applicable) where we can find the company colour scheme. Cards can be horizontal or vertical format.
We are looking for a two sided business card - on the front we will see the personal details of the employee (name, position, email and phone number), and then on the back, we will see the business details (name and logo, address, phone number, website, email, company tagline: "Accelerating technology disruption in the automotive market")
We want the design to be clean and simple, but also fun, modern, and capturing of a young startup vibe.

```html
<!DOCTYPE html>
<html lang="en">
<head>
<meta charset="utf-8">
<title>Korimet Business Cards</title>
<link rel="stylesheet" href="https://fonts.googleapis.com/css2?family=Arimo:wght@400;700&family=Montserrat:wght@500;700&display=swap">
<style>
  :root {
    --brand-violet: #4637c3;
    --brand-violet-deep: #3d2fb4;
    --card-white: #f0eff0;
    --ink: #2b2b2e;
    --paper-bg: #2a2a2c;
    --white: #ffffff;
  }
  * { box-sizing: border-box; margin: 0; padding: 0; }
  html, body { width: 1200px; height: 1015px; overflow: hidden; }
  body {
    background: var(--paper-bg);
    display: flex;
    flex-direction: column;
    align-items: center;
    justify-content: center;
    gap: 56px;
    font-family: "Arimo", Arial, sans-serif;
  }
  .card {
    width: 700px;
    height: 400px;
    position: relative;
    overflow: hidden;
    box-shadow: 0 14px 30px rgba(0,0,0,.45);
  }

  /* Company side */
  .card--company { background: var(--card-white); }
  .company-mark {
    position: absolute;
    top: 78px; left: 0; right: 0;
    display: flex; align-items: center; justify-content: center; gap: 16px;
  }
  .company-mark__dot {
    width: 42px; height: 42px; border-radius: 50%;
    background: var(--brand-violet);
  }
  .company-mark__name {
    font-family: "Montserrat", Arial, sans-serif;
    font-weight: 700;
    font-size: 58px;
    letter-spacing: 1px;
    color: var(--brand-violet);
    text-transform: lowercase;
  }
  .company-details {
    position: absolute;
    top: 200px; left: 0; right: 0;
    text-align: center;
    color: var(--ink);
    font-size: 17px;
    letter-spacing: .3px;
  }
  .company-details__address { margin-bottom: 12px; }
  .company-details__rule {
    width: 62px; height: 1.5px; margin: 0 auto 14px;
    background: var(--brand-violet);
  }
  .company-details__label { color: var(--brand-violet); font-weight: 700; }
  .company-details__link { color: var(--brand-violet); }
  .tagline-band {
    position: absolute; left: 0; right: 0; bottom: 0;
    height: 64px;
    background: var(--brand-violet);
    display: flex; align-items: center; justify-content: center;
    color: var(--white);
    font-size: 16.5px;
    letter-spacing: .6px;
    text-transform: uppercase;
  }

  /* Personal side */
  .card--personal { background: var(--brand-violet); }
  .wordmark-texture {
    position: absolute; inset: 0;
    background: radial-gradient(ellipse at 50% 50%, var(--brand-violet) 0%, var(--brand-violet-deep) 100%);
  }
  .personal-details {
    position: absolute; inset: 0;
    display: flex; flex-direction: column; align-items: center; justify-content: center;
    color: var(--white);
    text-align: center;
  }
  .personal-details__name {
    font-family: "Montserrat", Arial, sans-serif;
    font-weight: 700;
    font-size: 30px;
    letter-spacing: .5px;
    text-transform: uppercase;
  }
  .personal-details__role { font-size: 19px; margin-top: 2px; }
  .personal-details__rule {
    width: 96px; height: 1.5px; background: var(--white);
    margin: 18px 0 20px;
  }
  .personal-details__contact { font-size: 19px; line-height: 1.45; letter-spacing: .3px; }
</style>
</head>
<body>

  <section class="card card--company" aria-label="Company side">
    <div class="company-mark">
      <span class="company-mark__dot"></span>
      <span class="company-mark__name">korimet</span>
    </div>
    <div class="company-details">
      <p class="company-details__address">27, Ridgeway Park Road 60817, Northland</p>
      <div class="company-details__rule"></div>
      <p class="company-details__contact">
        <span class="company-details__label">P:</span> 044-318 270 564 |
        <span class="company-details__label">E:</span> hello@korimet.io |
        www.<span class="company-details__link">korimet</span>.io
      </p>
    </div>
    <div class="tagline-band">Accelerating technology disruption in the automotive market</div>
  </section>

  <section class="card card--personal" aria-label="Personal side">
    <div class="wordmark-texture" role="img" aria-label="Embossed repeating company wordmark texture across the card"></div>
    <div class="personal-details">
      <h1 class="personal-details__name">Marcus Hale</h1>
      <p class="personal-details__role">Managing Director</p>
      <div class="personal-details__rule"></div>
      <p class="personal-details__contact">hello@korimet.io<br>www.korimet.io</p>
    </div>
  </section>

</body>
</html>
```